Awesome new dental practice requires a New Letterhead design

We would like a new letterhead design to align with our new business branding & business cards. I have uploaded all the logos & current business card details that can be used. The new website can be viewed here https://kelvora.com.au

Other useful details: Font Poppins
Colour Palettes:
Dark Pink #c45389
Light Pink: #e83e8c
Black

Please let me know if you have any questions or require anything else.

Dental

• Poppins

```html
<!DOCTYPE html>
<html lang="en">
<head>
<meta charset="utf-8">
<title>Kelvora Letterhead</title>
<link rel="stylesheet" href="https://fonts.googleapis.com/css2?family=Poppins:wght@400;500;600&family=Open+Sans:wght@400&display=swap">
<style>
  :root {
    --pink-dark: #c45389;
    --pink-light: #e83e8c;
    --black: #141414;
    --ink: #444444;
    --paper: #f8f8f8;
    --backdrop: #dcdcdc;
    --placeholder: #e6e6e6;
  }
  * { margin: 0; padding: 0; box-sizing: border-box; }
  html, body {
    width: 1153px; height: 1200px; overflow: hidden;
    background: var(--backdrop);
  }
  .letterhead {
    position: absolute; left: 146px; top: 0;
    width: 860px; height: 1200px;
    background: var(--paper);
    overflow: hidden;
  }
  .brand {
    position: absolute; left: 92px; top: 110px;
    display: flex; align-items: center; gap: 12px;
    font-family: "Poppins", sans-serif; font-weight: 600;
    font-size: 44px; line-height: 1; color: var(--black);
    letter-spacing: -0.5px;
  }
  .brand-mark {
    width: 16px; height: 16px; background: var(--pink-dark);
  }
  .contact {
    position: absolute; left: 563px; top: 79px;
    font-family: "Poppins", sans-serif; font-size: 15px;
    line-height: 20px; color: var(--ink);
  }
  .contact .address { margin-bottom: 8px; }
  .contact-row { display: flex; align-items: center; gap: 6px; height: 23px; }
  .contact-row svg { width: 15px; height: 15px; flex: none; }
  .letter {
    position: absolute; left: 77px; top: 268px; width: 705px;
    font-family: "Open Sans", sans-serif; font-size: 16px;
    line-height: 23px; color: var(--ink);
  }
  .letter p { margin-bottom: 23px; text-align: justify; }
  .letter .salutation, .letter .closing { text-align: left; }
  .signature-area {
    position: absolute; left: 78px; top: 873px;
    width: 102px; height: 98px; background: var(--placeholder);
  }
  .footer-band {
    position: absolute; left: 0; bottom: 0; width: 860px; height: 41px;
  }
  .footer-band svg { position: absolute; inset: 0; }
  .tagline {
    position: absolute; left: 0; width: 836px; top: 0; height: 41px;
    display: flex; align-items: center; justify-content: center;
    font-family: "Poppins", sans-serif; font-weight: 500; font-size: 16px;
    letter-spacing: 2px; color: #ffffff;
  }
  .tagline .accent { color: var(--pink-light); }
</style>
</head>
<body>
  <main class="letterhead">
    <header>
      <div class="brand"><span class="brand-mark"></span>Kelvora</div>
      <address class="contact" style="font-style:normal">
        <div class="address">Shop 9, 27 Marlowe Street<br>Port Hedland WA</div>
        <div class="contact-row">
          <svg viewBox="0 0 16 16"><path fill="var(--pink-dark)" d="M3.5 1.5l2.5 0 1 3.5-1.8 1.3a8 8 0 0 0 4.5 4.5L11 9l3.5 1v2.5c0 1-1 2-2 2C6.5 14.5 1.5 9.5 1.5 3.5c0-1 1-2 2-2z"/></svg>
          <span>(08) 9046 2187</span>
        </div>
        <div class="contact-row">
          <svg viewBox="0 0 16 16"><rect x="1" y="3" width="14" height="10" rx="1" fill="var(--pink-dark)"/><path d="M1.5 4l6.5 5 6.5-5" fill="none" stroke="#fff" stroke-width="1.3"/></svg>
          <span>hello@kelvora.com</span>
        </div>
        <div class="contact-row">
          <svg viewBox="0 0 16 16"><circle cx="8" cy="8" r="7" fill="var(--pink-dark)"/><path d="M4 5c2 0 3 1 2.5 2.5S4 9 5 11M10 3c-1 2 1 3 2.5 3M9 13c0-2 2-2 3-3.5" fill="none" stroke="#fff" stroke-width="1.1"/></svg>
          <span>www.kelvora.com.au</span>
        </div>
      </address>
    </header>

    <section class="letter">
      <p class="salutation">Dear customer,</p>
      <p>Lorem ipsum dolor sit amet, consectetur adipisicing elit, sed do eiusmod tempor incididunt ut labore et dolore magna aliqua. Ut enim ad minim veniam, quis nostrud exercitation ullamco laboris nisi ut aliquip ex ea commodo consequat. Duis aute irure dolor in reprehenderit in voluptate velit esse cillum dolore eu fugiat nulla pariatur. Excepteur sint occaecat cupidatat non proident, sunt in culpa qui officia deserunt mollit anim id est laborum.</p>
      <p>Lorem ipsum dolor sit amet, consectetur adipisicing elit, sed do eiusmod tempor incididunt ut labore et dolore magna aliqua. Ut enim ad minim veniam, quis nostrud exercitation ullamco laboris nisi ut aliquip ex ea commodo consequat. Duis aute irure dolor in reprehenderit in voluptate velit esse cillum dolore eu fugiat nulla pariatur. Excepteur sint occaecat cupidatat non proident, sunt in culpa qui officia deserunt mollit anim id est laborum.</p>
      <p>Lorem ipsum dolor sit amet, consectetur adipisicing elit, sed do eiusmod tempor incididunt ut labore et dolore magna aliqua. Ut enim ad minim veniam, quis nostrud exercitation ullamco laboris nisi ut aliquip ex ea commodo consequat. Duis aute irure dolor in reprehenderit in voluptate velit esse cillum dolore eu fugiat nulla pariatur. Excepteur sint occaecat cupidatat non proident, sunt in culpa qui officia deserunt mollit anim id est laborum.</p>
      <p>Lorem ipsum dolor sit amet, consectetur adipisicing elit, sed do eiusmod tempor incididunt ut labore et dolore magna aliqua. Ut enim ad minim veniam, quis nostrud exercitation ullamco laboris nisi ut aliquip ex ea commodo consequat. Duis aute irure dolor in reprehenderit.</p>
      <p class="closing">Yours Sincerely,</p>
    </section>

    <div class="signature-area" role="img" aria-label="Handwritten signature of the sender"></div>

    <footer class="footer-band">
      <svg width="860" height="41" viewBox="0 0 860 41">
        <polygon points="0,0 814,0 836,41 0,41" fill="var(--black)"/>
      </svg>
      <p class="tagline">Life is short.&nbsp;<span class="accent">Smile</span>&nbsp;while Still have teeth.</p>
    </footer>
  </main>
</body>
</html>
```